Open Horizon; Teaching Series Art.

Our church is going to be teaching a series of messages under the topic/title: Open Horizon. Just looking for a simple design to help with this. I have uploaded a design that is an example of what we were thinking.

The point of the design is to communicate a new way of doing things (given some of the impact of the coronavirus) - although the background doesn't need to be too busy - just something simple, clean and modern.

Even though it's for a church, we don't need any religious art in the background (crosses, people praying, etc.) Looking for a similar feel background to the one we uploaded.

The only text should be Open Horizon and maybe highlighting the word Open somehow.

Font styles to use
Sans Serif

Requirements
Must have
• Title of "Open Horizon" - no other text.

```html
<!DOCTYPE html>
<html lang="en">
<head>
<meta charset="UTF-8">
<title>Open Horizon</title>
<link rel="stylesheet" href="https://fonts.googleapis.com/css2?family=Montserrat:wght@800&display=swap">
<style>
  :root {
    --sky-top: #6a3a5a;
    --sky-ember: #e0452a;
    --sky-orange: #f4792c;
    --sky-glow: #fbd27a;
    --horizon-haze: #e9c9bf;
    --sea-light: #9fb0c8;
    --sea-mid: #4f6a92;
    --sea-deep: #0e1d3c;
    --accent-red: rgba(205, 62, 48, 0.88);
    --accent-slate: rgba(104, 108, 138, 0.88);
    --title-white: #ffffff;
  }
  * { margin: 0; padding: 0; box-sizing: border-box; }
  html, body { width: 1200px; height: 675px; overflow: hidden; }
  .series-art {
    position: relative;
    width: 1200px;
    height: 675px;
    overflow: hidden;
  }
  .seascape {
    position: absolute;
    inset: 0;
    background:
      radial-gradient(ellipse 55% 22% at 58% 52%, rgba(255, 226, 150, 0.6), rgba(255, 226, 150, 0) 70%),
      linear-gradient(to bottom,
        var(--sky-top) 0%,
        var(--sky-ember) 18%,
        var(--sky-orange) 36%,
        var(--sky-glow) 50%,
        var(--horizon-haze) 55.5%,
        var(--sea-light) 60%,
        var(--sea-mid) 75%,
        var(--sea-deep) 100%);
  }
  .series-title {
    position: absolute;
    left: 269px;
    top: 271px;
    display: flex;
    height: 86px;
  }
  .title-word {
    display: flex;
    align-items: center;
    justify-content: center;
    height: 100%;
    font-family: "Montserrat", sans-serif;
    font-weight: 800;
    font-size: 74px;
    line-height: 1;
    letter-spacing: 2px;
    color: var(--title-white);
    text-shadow: 0 1px 2px rgba(0, 0, 0, 0.25);
    white-space: nowrap;
  }
  .title-word--highlight { width: 235px; background: var(--accent-red); }
  .title-word--rest { width: 426px; background: var(--accent-slate); }
</style>
</head>
<body>
  <main class="series-art">
    <div class="seascape" role="img" aria-label="Fiery orange and red sunset sky over a calm blue sea"></div>
    <h1 class="series-title">
      <span class="title-word title-word--highlight">OPEN</span>
      <span class="title-word title-word--rest">HORIZON</span>
    </h1>
  </main>
</body>
</html>
```